Web Design Project

We need a website design for our marketing agency: loftwaveo.com.au

We want something that is eye-catching and will wow audiences, yet at the same time it cannot turn-off corporate clients. The website should be highly focused on conversions with numerous call to actions on each page.

We like blue as our primary colour and have a mascot (the spider on the current website)

Target Market(s)

small business owners
small corporations
enterprise level business clients

Industry/Entity Type

Marketing

Requirements
Must have
• must incorporate the agency mascot (the spider on the website)

```html
<!DOCTYPE html>
<html lang="en">
<head>
<meta charset="utf-8">
<title>Loftwaveo – High ROI Digital Marketing</title>
<link href="https://fonts.googleapis.com/css2?family=Ubuntu:wght@400;500;700&family=Open+Sans:wght@400&family=Arimo:wght@400&family=Didact+Gothic&display=swap" rel="stylesheet">
<style>
:root{
  --sky:#8fc3e8;
  --sky-light:#a9d3f0;
  --sky-dark:#79b2dc;
  --accent:#29abe2;
  --accent-dark:#1891c8;
  --nav:#4a5968;
  --nav-dark:#2f3b47;
  --ink:#1e1e1e;
  --body:#222;
  --muted:#7a7a7a;
  --panel:#ffffff;
  --footer:#1f2124;
  --footer-light:#2d3034;
  --footer-text:#c9c9c9;
  --teal:#5fc9b8;
  --hero-top:#6e9fd4;
  --hero-bottom:#b7d3ec;
}
*{margin:0;padding:0;box-sizing:border-box}
html,body{width:1030px;height:1200px;overflow:hidden}
body{
  position:relative;
  background:linear-gradient(180deg,var(--sky-light) 0%,var(--sky) 40%,var(--sky-dark) 100%);
  font-family:'Arimo',Arial,sans-serif;
  color:var(--body);
}
.abs{position:absolute}

/* header */
.brand{left:150px;top:8px;display:flex;align-items:center;gap:10px}
.brand-mark{width:60px;height:60px;border-radius:50%;background:var(--nav-dark)}
.brand-name{font-family:'Ubuntu',sans-serif;font-weight:700;font-size:42px;color:var(--teal);letter-spacing:1px}
.tagline{left:223px;top:62px;font-family:'Ubuntu',sans-serif;font-weight:700;font-size:15px;color:#e9f4fb;letter-spacing:.5px}
.call{left:584px;top:28px;display:flex;align-items:center;gap:8px;font-family:'Ubuntu',sans-serif;font-size:17px;color:#3a4652}
.nav{left:221px;top:94px;display:flex;gap:5px}
.nav a{
  display:block;height:25px;line-height:25px;text-align:center;text-decoration:none;
  font-family:'Ubuntu',sans-serif;font-size:13.5px;color:#eef2f5;border-radius:3px;
  background:linear-gradient(180deg,var(--nav) 0%,var(--nav-dark) 100%);
  box-shadow:0 1px 2px rgba(0,0,0,.35);
}
.nav a.current{background:linear-gradient(180deg,#5cc9f5 0%,var(--accent-dark) 100%);color:#0d2a3a}

/* hero panel */
.hero{left:94px;top:146px;width:841px;height:395px;background:var(--panel);border-radius:8px;box-shadow:0 2px 6px rgba(0,0,0,.25);overflow:hidden}
.hero-visual{position:absolute;left:2px;top:2px;right:2px;height:284px;border-radius:6px 6px 0 0;
  background:linear-gradient(180deg,var(--hero-top) 0%,var(--hero-bottom) 100%)}
.slide-arrows{position:absolute;right:26px;top:275px;display:flex;gap:12px}
.slide-arrows span{width:22px;height:22px;border-radius:50%;background:linear-gradient(180deg,#fff,#c9ced3);box-shadow:0 1px 2px rgba(0,0,0,.4);display:flex;align-items:center;justify-content:center}
.hero-title{position:absolute;left:27px;top:309px;font-family:'Open Sans',sans-serif;font-weight:400;font-size:22px;line-height:26px;color:var(--ink)}
.hero-title em{font-style:normal;color:var(--accent)}
.hero-text{position:absolute;left:27px;top:336px;width:790px;font-size:10.5px;line-height:16px;text-align:justify;color:#333}

/* services panel */
.services{left:94px;top:590px;width:841px;height:342px;border-radius:8px;
  background:linear-gradient(180deg,#e9e9e9 0%,#f7f7f7 60%,#fff 100%);box-shadow:0 2px 6px rgba(0,0,0,.25)}
.feature{position:absolute;left:14px;width:167px}
.feature-visual{width:167px;height:90px}
.feature h3{font-family:'Ubuntu',sans-serif;font-weight:400;font-size:17px;color:var(--ink);margin:12px 0 0 2px}
.feature a{display:block;text-align:right;font-family:'Ubuntu',sans-serif;font-size:11px;color:var(--muted);margin-top:5px}
.column{position:absolute;top:16px;width:195px}
.column-visual{position:relative;height:87px;background:linear-gradient(180deg,#e1e1e1,#fafafa 70%,#e9e9e9);display:flex;justify-content:center;padding-top:14px}
.column-tag{position:absolute;left:0;bottom:0;background:var(--accent);color:#fff;font-family:'Ubuntu',sans-serif;font-size:10px;padding:2px 6px 1px}
.column h3{font-family:'Ubuntu',sans-serif;font-weight:500;font-size:15.5px;color:var(--ink);margin:7px 0 0 2px;line-height:16px}
.column p{font-size:10.7px;line-height:12.9px;color:var(--body);margin-left:2px}

/* footer */
.footer{left:0;top:993px;width:1030px;height:207px;background:linear-gradient(180deg,var(--footer-light) 0%,var(--footer) 100%)}
.footer-mark{position:absolute;left:128px;top:28px;width:110px;height:110px;border-radius:50%;background:#26292d}
.footer-name{position:absolute;left:279px;top:22px;font-family:'Ubuntu',sans-serif;font-weight:700;font-size:40px;color:var(--teal)}
.footer-call{position:absolute;left:279px;top:73px;font-family:'Ubuntu',sans-serif;font-size:14px;color:#a8a8a8}
.footer-address{position:absolute;left:279px;top:109px;font-family:'Didact Gothic',sans-serif;font-size:13px;line-height:15px;color:var(--footer-text);font-style:normal}
.audit-text{position:absolute;left:510px;top:36px;width:410px;font-family:'Didact Gothic',sans-serif;font-size:13px;line-height:15px;color:#e1e1e1}
.field{position:absolute;font-family:'Didact Gothic',sans-serif;font-size:13px;color:#e1e1e1}
.field span{display:block;margin-bottom:3px}
.field i{display:block;height:20px;border-radius:4px;background:linear-gradient(180deg,#4b4f55,#6a6f76);box-shadow:inset 0 2px 3px rgba(0,0,0,.6),0 1px 0 rgba(255,255,255,.15)}
</style>
</head>
<body>

<header>
  <div class="abs brand"><span class="brand-mark"></span><span class="brand-name">Loftwaveo</span></div>
  <div class="abs tagline">HIGH ROI DIGITAL MARKETING</div>
  <div class="abs call">
    <svg width="30" height="30" viewBox="0 0 30 30"><circle cx="15" cy="15" r="14" fill="#c8d3dc" stroke="#8c99a5"/><path d="M10 8c-2 2-1 6 3 10s8 5 10 3l-3-3-2 1c-2-1-4-3-5-5l1-2z" fill="#5f6d79"/></svg>
    Call Us Now: (+617) 3000 4820
  </div>
  <nav class="abs nav">
    <a class="current" style="width:75px">Home</a>
    <a style="width:74px">Services</a>
    <a style="width:74px">Blog</a>
    <a style="width:92px">SEO Pricing</a>
    <a style="width:74px">SEM</a>
    <a style="width:115px">About Loftwaveo</a>
    <a style="width:116px">Contact Loftwaveo</a>
  </nav>
</header>

<section class="abs hero">
  <div class="hero-visual" role="img" aria-label="Slideshow image: fantasy landscape scene"></div>
  <div class="slide-arrows">
    <span><svg width="8" height="8"><path d="M6 0L1 4l5 4z" fill="#333"/></svg></span>
    <span><svg width="8" height="8"><path d="M2 0l5 4-5 4z" fill="#333"/></svg></span>
  </div>
  <h1 class="hero-title">We are <em>leaders in</em>-Print , Media and web development</h1>
  <p class="hero-text">Ipasco lorames opus dalakom dolor sit amet, consectetur adipiscing elit. Aliquam velit dolor, luctus sit amet ultricies vitae, pellentesque in risus. Donec non massa tempus elit adipiscing.Praesent non justo risus, nec blandit sapien.</p>
</section>

<section class="abs services">
  <div class="feature" style="top:16px">
    <div class="feature-visual" role="img" aria-label="Photo of a sports car beside printed marketing material" style="background:linear-gradient(135deg,#d9d9d9,#2a2a2a 60%,#8a6a4a)"></div>
    <h3>SEO Services</h3>
    <a>find out more</a>
  </div>
  <div class="feature" style="top:164px">
    <div class="feature-visual" role="img" aria-label="Photo of a printed brochure with a colourful graphic" style="background:linear-gradient(135deg,#f2efe8,#e0a23a 55%,#3b8fd0 80%,#1b1b1b)"></div>
    <h3>SEO Brisbane</h3>
    <a>find out more</a>
  </div>

  <div class="column" style="left:208px">
    <div class="column-visual">
      <svg width="58" height="58" viewBox="0 0 58 58"><circle cx="29" cy="29" r="29" fill="#3a3a3a"/><rect x="16" y="18" width="24" height="17" rx="2" fill="none" stroke="#fff" stroke-width="3"/><rect x="13" y="37" width="32" height="4" rx="1" fill="#fff"/></svg>
      <span class="column-tag">Online Ad Management</span>
    </div>
    <h3>Online Ad Management</h3>
    <p>Need highly targeted traffic right now? Then let us help! We have a whole range of online advertising solutions, from Searchly Ads to Friendbook Ads to interactive banner Ads. Ad copy, creatives design &amp; conversion optimization – we can handle everything and get you the highest ROI for your ad dollar.</p>
  </div>
  <div class="column" style="left:419px">
    <div class="column-visual" role="img" aria-label="Dark butterfly illustration">
      <svg width="70" height="60"><circle cx="35" cy="30" r="28" fill="#2e2e2e"/></svg>
      <span class="column-tag">SEO Packages</span>
    </div>
    <h3>SEO Packages</h3>
    <p>Drive quality traffic to your business and boost your revenue. We offer high quality SEO packages at competitive rates with GUARANTEED results. Whether you’re a local business or a national enterprise, we can help your business grow.</p>
  </div>
  <div class="column" style="left:628px">
    <div class="column-visual" role="img" aria-label="Dark round emblem illustration">
      <svg width="60" height="60"><circle cx="30" cy="30" r="29" fill="#333"/></svg>
      <span class="column-tag">Social Media</span>
    </div>
    <h3>Social Media</h3>
    <p>Need to engage your target market? Want build your brand to create a loyal base of supporters for your business? Then social media is your solution. We can advise which social media options are right for your business – and there are way more options than just Friendbook and Chirper!</p>
  </div>
</section>

<footer class="abs footer">
  <span class="footer-mark"></span>
  <div class="footer-name">Loftwaveo</div>
  <div class="footer-call">Call Us Now: (+617) 3000 4820</div>
  <address class="footer-address">Address<br>Level 12, Harbour Point,<br>48 Quay Street,<br>Brisbane, Qld, 4000</address>
  <p class="audit-text">Fill in your details to get an SEO Audit (worth $500) to improve your website’s performance. It’s FREE but only until December 30!</p>
  <label class="field" style="left:515px;top:90px;width:154px"><span>Name</span><i></i></label>
  <label class="field" style="left:685px;top:90px;width:223px"><span>e-mail:</span><i></i></label>
  <label class="field" style="left:515px;top:139px;width:154px"><span>Phone:</span><i></i></label>
  <label class="field" style="left:685px;top:139px;width:223px"><span>website url:</span><i></i></label>
</footer>

</body>
</html>
```